Movie Poster, DVD Cover, Web Banner

I need to have a Movie Poster / DVD cover / designed for a family-friendly mystery movie.

Files need to be Adobe Photoshop or Illustrator files with all layers intact and editable.

The movie is a family-friendly murder mystery in the style of the movies on the Bramblewood Films and Puzzles cable channel.

The title of the movie is:
"Cedar Hollow Capers: Flames and Uh Ohs"

Tagline (optional)
"Moving back home... can be murder."

The style should match the look of the items on this Pinboardly page: https://www.pinboardly.example/lorvenatessi/bramblewood-mystery-movies/

You can see a movie trailer at this ClipTube link to get ideas about the tone of the film. https://www.cliptube.example/watch?v=qZr8wEfxPaM&t=1s

UPDATE: I am providing core artwork. Try to use one of the backgrounds provided, or something similar. Another option might be an interior with bookshelves.

POSTER:
DIMENSIONS: 24” x 36”
DPI: 300

DVD CASE: (Front Only)
DIMENSIONS: 7.2 " x 5"
DPI: 300

WEB BANNER:
DIMENSIONS: 1900 x 1080 pixels

I retain all rights to the artwork, but the artist will receive a credit on the movie.

Target Market(s)

Female TV audience for Mystery/Romance books and movies

Industry/Entity Type

Movie Production

Colors
6b449b
33b8a4
fac994

Requirements
Must have
• UPDATE: I am providing core artwork. Try to use one of the backgrounds provided, or something similar. Another option might be an interior with bookshelves. I have provided RAW .CR2 files so you can adjust the backgrounds as much as possible.
Nice to have
• Adjust and smooth the model's skin tone and coloring to look softer and more "film-like", like the way a portrait photographer retouches skin tones.

```html
<!DOCTYPE html>
<html lang="en">
<head>
<meta charset="utf-8">
<title>Cedar Hollow Capers: Flames and Uh Ohs — Web Banner</title>
<link rel="stylesheet" href="https://fonts.googleapis.com/css2?family=Montserrat:wght@800;900&family=Yellowtail&family=Lato:wght@400&family=Playball&display=swap">
<style>
  :root {
    --page: #ffffff;
    --tunnel-deep: #0b2a2e;
    --tunnel-mid: #1d4a4f;
    --tunnel-light: #3f6b6e;
    --glow-red: #c4141b;
    --band-red: #b3161c;
    --title-white: #ffffff;
    --script-orange: #f7a21b;
    --coat-purple: #5a2d8a;
    --hair-auburn: #8a4a24;
  }
  * { margin: 0; padding: 0; box-sizing: border-box; }
  html, body { width: 1200px; height: 1200px; overflow: hidden; background: var(--page); }
  .canvas { position: relative; width: 1200px; height: 1200px; background: var(--page); }

  .banner {
    position: absolute; left: 0; top: 258px; width: 1200px; height: 684px; overflow: hidden;
    background:
      radial-gradient(ellipse 260px 140px at 800px 360px, rgba(196,20,27,.75), rgba(196,20,27,0) 70%),
      radial-gradient(ellipse 520px 420px at 560px 380px, var(--tunnel-light), rgba(63,107,110,0) 70%),
      linear-gradient(180deg, var(--tunnel-mid) 0%, var(--tunnel-deep) 100%);
  }

  .heroine {
    position: absolute; left: 696px; top: 6px; width: 504px; height: 678px;
    background: linear-gradient(180deg, var(--hair-auburn) 0%, #7a4a3a 40%, var(--coat-purple) 62%, #4a2275 100%);
    border-radius: 220px 220px 0 0;
  }

  .title {
    position: absolute; left: 106px; color: var(--title-white);
    font-family: "Montserrat", sans-serif; font-weight: 900; line-height: 1;
    letter-spacing: -2px; text-transform: uppercase;
  }
  .title--top { top: 52px; font-size: 136px; }
  .title--bottom { top: 204px; font-size: 98px; letter-spacing: -1px; }

  .title-script {
    position: absolute; left: 206px; top: 262px; color: var(--script-orange);
    font-family: "Yellowtail", cursive; font-size: 150px; line-height: 1;
    transform: rotate(-6deg); transform-origin: left center;
  }

  .subtitle-streak {
    position: absolute; left: 300px; top: 398px; width: 360px; height: 44px;
    background: linear-gradient(90deg, rgba(179,22,28,0) 0%, var(--band-red) 35%, rgba(179,22,28,.6) 80%, rgba(179,22,28,0) 100%);
    transform: rotate(-5deg);
  }
  .subtitle {
    position: absolute; left: 362px; top: 396px; color: var(--title-white);
    font-family: "Lato", sans-serif; font-size: 29px; transform: rotate(-5deg); transform-origin: left center;
  }

  .tagline-band { position: absolute; left: 112px; top: 546px; width: 536px; height: 116px; }
  .tagline {
    position: absolute; left: 112px; top: 560px; width: 536px; text-align: center;
    color: var(--title-white); font-family: "Playball", cursive; font-size: 36px; line-height: 1.05;
  }
</style>
</head>
<body>
<main class="canvas">
  <section class="banner">
    <div class="heroine" role="img" aria-label="Photo of the lead actress, a red-haired woman in a purple trench coat with arms crossed"></div>

    <h1 class="title title--top">Cedar</h1>
    <h1 class="title title--bottom">Hollow</h1>
    <div class="title-script">capers</div>

    <div class="subtitle-streak"></div>
    <p class="subtitle">Flames and Uh Ohs"</p>

    <svg class="tagline-band" viewBox="0 0 536 116" aria-hidden="true">
      <path d="M6 18 L520 8 L530 30 L512 44 L536 60 L518 86 L528 104 L40 114 L56 96 L20 86 L32 68 L0 52 L24 36 Z" fill="var(--band-red)"/>
    </svg>
    <p class="tagline">“Moving back home...<br>can be murder.”</p>
  </section>
</main>
</body>
</html>
```